strength and conditioning business focused on helping people move more efficiently

I need a business card designed for a Philadelphia based company called Brk Stn Motion (pronounced Brick Stone). We offer fitness professional services with the idea of helping people feel better and move optimally. We do this by designing and walking through individualized programs as well as minor soft tissue work. Our perfect client would be athletes but we will be marketing to parents who have children that are active They remember their former athletic days and want to get as close as possible back to that feeling. Attached will be the official logo and logo formats. I would love for the design to communicate trustworthy and creative. I would also love for the design to be square with rounded edges.

Target Market(s)

Parents of athletic children
former athletes
athletes

Industry/Entity Type

Fitness

Contact Information for Business Card

Business: Brk Stn Athletics
Name: Coach Gareth Milford
Position: Strength and Conditioning Coach / Certified Personal Trainer
Contact: coach.mil@brkstn.example
Text: (555)204-7719

Font styles to use
Serif
Sans Serif

Colors
fbee38
fbee3e
0255a3
3176b5
ffffff

Requirements
Must have
• use of logo
Nice to have
• Square design
rounded edges

```html
<!DOCTYPE html>
<html lang="en">
<head>
<meta charset="utf-8">
<title>Brk Stn Motion – Business Card</title>
<link href="https://fonts.googleapis.com/css2?family=Nunito:wght@900&family=Arimo:wght@400;700&display=swap" rel="stylesheet">
<style>
  :root {
    --stage: #2b2b2b;
    --card-white: #ffffff;
    --brand-blue: #0c3586;
    --brand-blue-light: #134099;
    --brand-yellow: #fcd307;
    --ink: #1e1e1e;
  }
  * { margin: 0; padding: 0; box-sizing: border-box; }
  html, body {
    width: 1200px; height: 859px; overflow: hidden;
    background: var(--stage);
  }
  .canvas { position: relative; width: 1200px; height: 859px; }
  .card {
    position: absolute; top: 208px;
    width: 446px; height: 445px; border-radius: 30px; overflow: hidden;
  }
  .card-front { left: 142px; background: var(--card-white); }
  .card-back {
    left: 626px;
    background: linear-gradient(135deg, var(--brand-blue-light), var(--brand-blue));
  }
  .brand-row {
    position: absolute; left: 26px; top: 92px;
    display: flex; align-items: center; gap: 14px;
  }
  .brand-mark {
    width: 50px; height: 50px; border-radius: 50%;
    border: 5px solid var(--brand-yellow);
  }
  .brand-name {
    font-family: "Nunito", sans-serif; font-weight: 900;
    font-size: 44px; line-height: 1; color: var(--brand-blue);
    letter-spacing: 0.5px;
  }
  .accent-bar {
    position: absolute; left: 0; top: 264px;
    width: 9px; height: 52px; background: var(--brand-blue);
  }
  .person {
    position: absolute; left: 24px; top: 262px;
    font-family: "Arimo", sans-serif; color: var(--ink);
  }
  .person-name { font-size: 19px; font-weight: 700; margin-bottom: 6px; }
  .person-name .first { color: var(--brand-yellow); }
  .person-name .last { color: var(--brand-blue); }
  .person-role { font-size: 14px; line-height: 19px; }
  .contacts {
    position: absolute; left: 24px; top: 357px; list-style: none;
    font-family: "Arimo", sans-serif; font-size: 14px; color: var(--ink);
  }
  .contacts li { display: flex; align-items: center; gap: 6px; height: 19px; }
  .contacts svg { width: 9px; height: 9px; fill: var(--brand-blue); }
  .back-mark {
    position: absolute; left: 177px; top: 64px;
    width: 92px; height: 92px; border-radius: 50%;
    border: 8px solid var(--brand-yellow);
  }
  .back-name {
    position: absolute; left: 0; right: 0; top: 170px;
    text-align: center;
    font-family: "Nunito", sans-serif; font-weight: 900;
    font-size: 76px; line-height: 82px; color: var(--card-white);
  }
</style>
</head>
<body>
<div class="canvas">
  <section class="card card-front">
    <div class="brand-row">
      <div class="brand-mark"></div>
      <div class="brand-name">Brk Stn Motion</div>
    </div>
    <div class="accent-bar"></div>
    <div class="person">
      <p class="person-name"><span class="first">Coach Gareth</span> <span class="last">Milford</span></p>
      <p class="person-role">Strength and Conditioning Coach /<br>Certified Personal Trainer</p>
    </div>
    <ul class="contacts">
      <li><svg viewBox="0 0 10 10"><path d="M2 0h2l1 3-1.5 1a6 6 0 0 0 2.5 2.5L7 5l3 1v2a2 2 0 0 1-2 2A8 8 0 0 1 0 2a2 2 0 0 1 2-2z"/></svg>(555)204-7719</li>
      <li><svg viewBox="0 0 10 10"><path d="M0 2h10v1L5 6 0 3zM0 4l5 3 5-3v4H0z"/></svg>coach.mil@brkstn.example</li>
      <li><svg viewBox="0 0 10 10"><circle cx="5" cy="5" r="5"/></svg>www.brkstn.example</li>
    </ul>
  </section>

  <section class="card card-back">
    <div class="back-mark"></div>
    <div class="back-name">Brk Stn<br>Motion</div>
  </section>
</div>
</body>
</html>
```